Consulting Group Needs a Graphic Design

We have created a unique, cyclical process to describe our company's philosophy on parenting to our clients. It is provided in the attached file. At the center of the graphic design, which includes all written words on the page, is an image of a gardener that we really like. We found it through a clipart service, but we are not able to trademark it as our own. We would like to create a similar image which includes the female gardener tending the garden, with a trowel in her hand and a watering can at her side. We want the flowers in her garden to be different, just as every child is unique and different within the same family. For more perspective on our company, please visit www.brookhavenfamilyway.com.
Updates

Project Deadline Extended
Reason: Some of the designers are getting very close to what we want. Due to some unforeseen circumstances, we were unable to give feedback for a couple of days. We would really appreciate your consideration of our request. We are eager to get the design finished to move forward with our branding strategy, so we will be hyper-focused on the project over the coming days. Thank you, Tillmore Family Consultants

Project Deadline Extended
Reason: We would like to give our first choice designer a chance to create a complementary logo to accompany his submission. We have been in communication with this designer.

Industry/Entity Type

Gardener

```html
<!DOCTYPE html>
<html lang="en">
<head>
<meta charset="utf-8">
<title>Every Good Gardener – Tillmore Family Consultants</title>
<link rel="stylesheet" href="https://fonts.googleapis.com/css2?family=Source+Sans+3:wght@400&display=swap">
<style>
  :root {
    --green-top: #356a33;
    --green-bottom: #4a9642;
    --accent: #f9b042;
    --node-fill: #ffffff;
    --ink: #111111;
    --scene-soil: #6b4a2b;
    --scene-grass: #7fae4f;
  }
  html, body {
    margin: 0;
    padding: 0;
    overflow: hidden;
  }
  .canvas {
    width: 1200px;
    height: 1000px;
    position: relative;
    overflow: hidden;
    background: linear-gradient(180deg, var(--green-top) 0%, var(--green-bottom) 100%);
    font-family: "Source Sans 3", "Myriad Pro", sans-serif;
  }
  .headline {
    position: absolute;
    top: 42px;
    left: 0;
    width: 1200px;
    margin: 0;
    text-align: center;
    font-weight: 400;
    font-size: 78px;
    line-height: 1;
    color: var(--accent);
  }
  .cycle {
    position: absolute;
    inset: 0;
  }
  .cycle-path, .cycle-arrow {
    fill: none;
    stroke: var(--accent);
    stroke-width: 5;
    stroke-linecap: round;
    stroke-linejoin: round;
  }
  .step-bubble {
    fill: var(--node-fill);
    stroke: var(--accent);
    stroke-width: 3;
  }
  .step-label {
    fill: var(--ink);
    font-size: 27px;
    text-anchor: middle;
  }
  .credit {
    position: absolute;
    left: 408px;
    top: 897px;
    width: 451px;
    height: 40px;
    border: 2px solid var(--accent);
    color: var(--accent);
    font-size: 21px;
    line-height: 40px;
    text-align: center;
  }
</style>
</head>
<body>
<div class="canvas">
  <h1 class="headline">Every Good Gardener :</h1>

  <svg class="cycle" width="1200" height="1000" viewBox="0 0 1200 1000">
    <defs>
      <radialGradient id="scene-tone" cx="50%" cy="60%" r="60%">
        <stop offset="0%" stop-color="#8a6a3c"/>
        <stop offset="55%" stop-color="#7fae4f"/>
        <stop offset="100%" stop-color="#5f9a45"/>
      </radialGradient>
    </defs>

    <ellipse class="cycle-path" cx="606" cy="532" rx="434" ry="292"/>

    <g role="img" aria-label="Illustration of a woman kneeling in her garden holding a trowel, with a watering can at her side and a variety of tulips, sunflowers and other flowers around her">
      <ellipse cx="580" cy="560" rx="210" ry="220" fill="url(#scene-tone)" opacity="0.9"/>
    </g>

    <!-- direction markers -->
    <polyline class="cycle-arrow" points="537,228 552,240 537,252"/>
    <polyline class="cycle-arrow" points="368,274 386,278 380,296" />
    <polyline class="cycle-arrow" points="918,312 934,334 914,344"/>
    <polyline class="cycle-arrow" points="986,644 1002,664 1018,648"/>
    <polyline class="cycle-arrow" points="522,808 500,820 522,834"/>
    <polyline class="cycle-arrow" points="150,580 168,560 186,576"/>

    <g class="step">
      <ellipse class="step-bubble" cx="646" cy="244" rx="91" ry="54"/>
      <text class="step-label" x="646" y="235">Plants with</text>
      <text class="step-label" x="646" y="272">purpose</text>
    </g>
    <g class="step">
      <ellipse class="step-bubble" cx="1001" cy="459" rx="91" ry="54"/>
      <text class="step-label" x="1001" y="469">Nurtures</text>
    </g>
    <g class="step">
      <ellipse class="step-bubble" cx="856" cy="759" rx="94" ry="56"/>
      <text class="step-label" x="856" y="750">Enriches</text>
      <text class="step-label" x="856" y="787">the soil</text>
    </g>
    <g class="step">
      <ellipse class="step-bubble" cx="259" cy="724" rx="92" ry="54"/>
      <text class="step-label" x="259" y="715">Prunes as</text>
      <text class="step-label" x="259" y="752">needed</text>
    </g>
    <g class="step">
      <ellipse class="step-bubble" cx="216" cy="365" rx="96" ry="54"/>
      <text class="step-label" x="216" y="356">Measures</text>
      <text class="step-label" x="216" y="393">growth</text>
    </g>
  </svg>

  <div class="credit">2009 Tillmore Family Consultants</div>
</div>
</body>
</html>
```